CalmPeak Nurses' Manifesto

Design a manifesto to inspire and motivate nurses to work at minimum standards of excellence in their nursing practice.

The manifesto will become a feature of our website, at conferences, workshops and retreats. It will also be featured on other marketing tools.

Primary Market:
Nurses and/or other healthcare professionals (specifically Doctors, Occupational Therapists, Psychologists and Social Workers).

However the manifesto is equally applicable to all nurses and healthcare professionals from new graduates to very experienced senior clinicians, administration officers,managers and healthcare executive personnel.

Mainly females and primarily 35 to 65 years old, which suggests people in this target age group have extensive experience, but have become jaded'.

The purpose of our business is to assist healthcare professionals, primarily nurses, to maintain their enthusiasm and excellence in service provision, for their benefit as well as the benefit of the clients.

I have attached:
File 1: Copy Samples and examples: which has the copy for the manifesto, examples that appeal to us and our 3 attempts.
File 2: Our colour Spec Sheet, HOWEVER the colours are not necessary limited to these colours. These colours are not in the logo that will be on the manifesto. The colours on the logo attached can/or also be used.
File 3: Prototype logo. The final logo will be available within 3 to 4 days.

Industry/Entity Type

Healthcare

Requirements
Must have
• Must use the copy as per the attached file.

It should be contemporary, eye catching and motivational.

Should not have
• MUST BE EASY TO READ. Each line MUST be clearly defined from each other.

```html
<!DOCTYPE html>
<html lang="en">
<head>
<meta charset="utf-8">
<title>CalmPeak Nurses' Manifesto</title>
<link rel="stylesheet" href="https://fonts.googleapis.com/css2?family=Bebas+Neue&family=Comfortaa:wght@300&family=Crimson+Text&family=Montserrat:wght@700&family=Nunito:wght@800;900&family=Oswald:wght@500;600&family=Pacifico&family=Parisienne&family=Quicksand:wght@300;400&display=swap">
<style>
  :root {
    --lime: #8cc540;
    --leaf: #22b04b;
    --coral: #f26b43;
    --teal: #1aa9a4;
    --white: #ffffff;
    --grey: #8a8a8a;
  }
  html, body { margin: 0; padding: 0; overflow: hidden; background: var(--white); }
  .manifesto { display: block; width: 849px; height: 1200px; }
  .title { font-family: "Bebas Neue", sans-serif; fill: var(--white); }
  .thin { font-family: "Quicksand", sans-serif; font-weight: 300; }
  .light { font-family: "Quicksand", sans-serif; font-weight: 400; }
  .condensed { font-family: "Oswald", sans-serif; font-weight: 500; }
  .condensed-bold { font-family: "Oswald", sans-serif; font-weight: 600; }
  .rounded { font-family: "Nunito", sans-serif; font-weight: 900; }
  .rounded-small { font-family: "Nunito", sans-serif; font-weight: 800; }
  .serif { font-family: "Crimson Text", serif; }
  .geo { font-family: "Montserrat", sans-serif; font-weight: 700; }
  .script-bold { font-family: "Pacifico", cursive; }
  .script-fine { font-family: "Parisienne", cursive; }
  .soft { font-family: "Comfortaa", sans-serif; font-weight: 300; }
  .fill-lime { fill: var(--lime); }
  .fill-leaf { fill: var(--leaf); }
  .fill-coral { fill: var(--coral); }
  .fill-teal { fill: var(--teal); }
  .fill-white { fill: var(--white); }
  .fill-grey { fill: var(--grey); }
</style>
</head>
<body>
<main>
<svg class="manifesto" viewBox="0 0 849 1200" xmlns="http://www.w3.org/2000/svg" role="img" aria-label="Nurses' Manifesto by CalmPeak for Nurses">

  <!-- Header band -->
  <rect class="fill-lime" x="0" y="0" width="849" height="163"/>
  <text class="title" x="25" y="131" font-size="124" textLength="795" lengthAdjust="spacingAndGlyphs">NURSES’ MANIFESTO</text>

  <!-- Open hands block -->
  <rect class="fill-coral" x="0" y="176" width="509" height="136"/>
  <text class="thin fill-white" x="30" y="250" font-size="58" textLength="460" lengthAdjust="spacingAndGlyphs">Nurse with open</text>
  <text class="thin fill-white" x="30" y="293" font-size="40" textLength="455" lengthAdjust="spacingAndGlyphs">hands, hearts and minds.</text>

  <!-- Health statement -->
  <text class="condensed fill-teal" x="517" y="193" font-size="18" textLength="305" lengthAdjust="spacingAndGlyphs">LOOK AFTER YOURSELF AND VALUE YOUR HEALTH</text>
  <text class="condensed fill-teal" x="517" y="227" font-size="36" textLength="305" lengthAdjust="spacingAndGlyphs">AS MUCH AS YOU VALUE THE</text>
  <text class="condensed fill-teal" x="517" y="270" font-size="47" textLength="305" lengthAdjust="spacingAndGlyphs">HEALTH OF OTHERS.</text>

  <!-- Delight block -->
  <rect class="fill-leaf" x="519" y="287" width="330" height="123"/>
  <text class="light fill-white" x="532" y="326" font-size="24" textLength="292" lengthAdjust="spacingAndGlyphs">Delight your clients and</text>
  <text class="light fill-white" x="532" y="356" font-size="24" textLength="290" lengthAdjust="spacingAndGlyphs">colleagues by exceeding</text>
  <text class="light fill-white" x="532" y="391" font-size="33" textLength="282" lengthAdjust="spacingAndGlyphs">their expectations.</text>

  <!-- Left column statements -->
  <text class="rounded fill-leaf" x="28" y="373" font-size="38" textLength="475" lengthAdjust="spacingAndGlyphs">DELIVER CARE SKILLFULLY.</text>

  <text class="serif fill-coral" x="30" y="440" font-size="44" textLength="465" lengthAdjust="spacingAndGlyphs">Support your colleagues</text>
  <text class="serif fill-coral" x="30" y="480" font-size="30" textLength="262" lengthAdjust="spacingAndGlyphs">and champion their</text>
  <text class="serif fill-coral" x="303" y="482" font-size="50" textLength="196" lengthAdjust="spacingAndGlyphs">purpose.</text>

  <text class="geo fill-teal" transform="translate(45 582) rotate(-90)" font-size="15" textLength="66" lengthAdjust="spacingAndGlyphs">RESPECT</text>
  <text class="geo fill-teal" x="55" y="532" font-size="20" textLength="383" lengthAdjust="spacingAndGlyphs">the limits of people’s knowledge</text>
  <text class="geo fill-teal" x="55" y="577" font-size="38" textLength="383" lengthAdjust="spacingAndGlyphs">and share your</text>
  <text class="geo fill-teal" x="55" y="607" font-size="25" textLength="383" lengthAdjust="spacingAndGlyphs">knowledge generously.</text>

  <text class="rounded fill-coral" x="28" y="655" font-size="30" textLength="412" lengthAdjust="spacingAndGlyphs">BE A LIFELONG LEARNER.</text>

  <text class="script-bold fill-lime" x="38" y="738" font-size="84" textLength="420" lengthAdjust="spacingAndGlyphs">Celebrate,</text>
  <text class="rounded-small fill-lime" x="35" y="772" font-size="15" textLength="405" lengthAdjust="spacingAndGlyphs">respect and value the diversity of Australian culture.</text>

  <!-- Learn block -->
  <text class="condensed-bold fill-leaf" x="520" y="505" font-size="104" textLength="192" lengthAdjust="spacingAndGlyphs">LEARN</text>
  <text class="condensed-bold fill-leaf" x="450" y="565" font-size="64" textLength="262" lengthAdjust="spacingAndGlyphs">SOMETHING</text>
  <text class="condensed-bold fill-leaf" x="450" y="615" font-size="60" textLength="262" lengthAdjust="spacingAndGlyphs">NEW EACH DAY.</text>

  <text class="condensed-bold fill-coral" x="470" y="660" font-size="30" textLength="245" lengthAdjust="spacingAndGlyphs">SEEK SUCCESS FIRSTLY</text>
  <text class="condensed-bold fill-coral" x="470" y="705" font-size="50" textLength="245" lengthAdjust="spacingAndGlyphs">FROM WITHIN</text>

  <!-- Trust (vertical) -->
  <text class="thin fill-lime" transform="translate(768 420) rotate(90)" font-size="40" textLength="300" lengthAdjust="spacingAndGlyphs">Trust your knowledge</text>
  <text class="thin fill-lime" transform="translate(748 420) rotate(90)" font-size="22" textLength="300" lengthAdjust="spacingAndGlyphs">and seek advice only from</text>
  <text class="thin fill-lime" transform="translate(718 420) rotate(90)" font-size="32" textLength="300" lengthAdjust="spacingAndGlyphs">respected sources.</text>

  <!-- Smile -->
  <text class="script-fine fill-teal" x="500" y="815" font-size="130" textLength="320" lengthAdjust="spacingAndGlyphs">Smile</text>
  <text class="rounded-small fill-teal" x="510" y="839" font-size="14" textLength="302" lengthAdjust="spacingAndGlyphs">and infect others with your happiness and have fun!</text>

  <!-- Can do -->
  <text class="serif fill-teal" x="35" y="810" font-size="30" textLength="246" lengthAdjust="spacingAndGlyphs">Adopt a ‘can do’</text>
  <text class="serif fill-teal" x="288" y="799" font-size="17" textLength="172" lengthAdjust="spacingAndGlyphs">attitude to everything</text>
  <text class="serif fill-teal" x="300" y="819" font-size="17" textLength="155" lengthAdjust="spacingAndGlyphs">that comes your way.</text>

  <!-- Unique (vertical) -->
  <text class="light fill-lime" transform="translate(80 1190) rotate(-90)" textLength="350" lengthAdjust="spacingAndGlyphs"><tspan font-size="34">You are </tspan><tspan font-size="58">unique</tspan></text>
  <text class="light fill-lime" transform="translate(108 1190) rotate(-90)" font-size="26" textLength="320" lengthAdjust="spacingAndGlyphs">revel in your individuality.</text>
  <text class="rounded fill-lime" transform="translate(134 1190) rotate(-90)" font-size="20" textLength="355" lengthAdjust="spacingAndGlyphs">Always be solution focused.</text>

  <!-- Lead -->
  <text class="condensed-bold fill-coral" x="155" y="843" font-size="20" textLength="305" lengthAdjust="spacingAndGlyphs">ONLY FOLLOW EXCEPTIONAL LEADERS.</text>
  <text class="condensed-bold fill-coral" x="155" y="868" font-size="20" textLength="310" lengthAdjust="spacingAndGlyphs">IF THERE IS NO ONE LEFT TO FOLLOW,</text>
  <text class="condensed-bold fill-coral" x="155" y="934" font-size="70" textLength="310" lengthAdjust="spacingAndGlyphs">THEN LEAD!</text>
  <text class="condensed-bold fill-coral" x="155" y="958" font-size="19" textLength="310" lengthAdjust="spacingAndGlyphs">ALWAYS LEAD WITH PURPOSE, PASSION</text>
  <text class="condensed-bold fill-coral" x="155" y="993" font-size="36" textLength="310" lengthAdjust="spacingAndGlyphs">AND COMMITMENT.</text>

  <!-- Right lower statements -->
  <text class="serif fill-coral" x="470" y="869" font-size="18" textLength="350" lengthAdjust="spacingAndGlyphs">Always do the right thing without exception.</text>
  <text class="soft fill-lime" x="473" y="903" font-size="30" textLength="350" lengthAdjust="spacingAndGlyphs">Choose your thoughts wisely,</text>
  <text class="soft fill-lime" x="473" y="940" font-size="30" textLength="350" lengthAdjust="spacingAndGlyphs">they create your reality.</text>
  <text class="condensed-bold fill-leaf" x="481" y="972" font-size="18" textLength="337" lengthAdjust="spacingAndGlyphs">RESPOND TO COMPLEX SITUATIONS INNOVATIVELY,</text>
  <text class="condensed-bold fill-leaf" x="481" y="993" font-size="13" textLength="340" lengthAdjust="spacingAndGlyphs">CREATIVELY AND SAFELY WITHIN THE SCOPE OF YOUR PRACTICE.</text>

  <!-- Dream block -->
  <rect class="fill-teal" x="212" y="1012" width="318" height="188"/>
  <text class="script-bold fill-white" x="262" y="1085" font-size="56" textLength="240" lengthAdjust="spacingAndGlyphs">Live your</text>
  <text class="script-bold fill-white" x="250" y="1170" font-size="72" textLength="260" lengthAdjust="spacingAndGlyphs">dream.</text>

  <!-- Brand name -->
  <circle class="fill-teal" cx="605" cy="1098" r="26"/>
  <text class="light fill-coral" x="645" y="1095" font-size="34">CalmPeak</text>
  <text class="light fill-coral" x="645" y="1130" font-size="26">For Nurses</text>

  <text class="light fill-grey" x="8" y="1195" font-size="8">© CALMPEAK FOR NURSES</text>
</svg>
</main>
</body>
</html>
```